Veteran Owned General Contractor needs Bold New Business Cards

We are a service disabled veteran owned small business. We're a general contractor that specializes in excavation, underground utilities, site work, land clearing and demolition. We would like a fresh, simple, bold, new look for our business cards. We're open to ideas! We'd like to incorporate the following information on the card:

Company Name & Logo, Name of Person, Job Title, Office Phone, Fax, Cell Phone, Email Address, Website, SDVOSB

Our logo is included. We look forward to your thoughts.

Thank you!
Updates

Reason: Hello Due to the overwhelming response to this project, we are extending the deadline one time to allow for improved communication and feedback with the top candidates. We would like to thank everyone for their hard work and exceptional creativity! Thank you

Industry/Entity Type

Business

Contact Information for Business Card

Font styles to use
Sans Serif

Requirements
Nice to have
• As we are a veteran owned company, it would be nice to incorporate an American flag into the design. Maybe on the back?

```html
<!DOCTYPE html>
<html lang="en">
<head>
<meta charset="utf-8">
<title>Ridgeline Inc — Business Card</title>
<link href="https://fonts.googleapis.com/css2?family=Ubuntu:wght@400;700&display=swap" rel="stylesheet">
<style>
  :root{
    --stage:#3a3a3a;
    --card-back:#2e2e2e;
    --card-face:#1f1f1f;
    --stripe-dark:#1c1c1c;
    --stripe-light:#262626;
    --canton:#232323;
    --frame-gray:#8a8b8d;
    --mark-fill:#222122;
    --faint:#3a3a3a;
    --faint-line:#444;
    --green:#6cc04a;
    --white:#ffffff;
    --text:#e6e6e6;
  }
  *{box-sizing:border-box;margin:0;padding:0}
  html,body{width:1200px;height:1000px;overflow:hidden}
  body{background:var(--stage);font-family:"Ubuntu",sans-serif;position:relative}

  .card{position:absolute;left:170px;width:860px;height:460px;overflow:hidden;border-radius:2px;box-shadow:0 6px 18px rgba(0,0,0,.45)}

  /* back of card */
  .card--back{top:25px;background:var(--card-back)}
  .card--back .brand{position:absolute;left:48px;bottom:52px;display:flex;align-items:center;gap:12px}
  .brand__square{width:40px;height:40px;border:3px solid var(--frame-gray);border-radius:6px;background:var(--mark-fill)}
  .brand__name{font-weight:700;font-size:34px;letter-spacing:2px;color:var(--green)}
  .faint-square{position:absolute;right:40px;top:40px;width:380px;height:380px;border-radius:36px;background:var(--faint);border:4px solid var(--faint-line)}
  .faint-square::after{content:"";position:absolute;inset:14px;border:2px solid var(--faint-line);border-radius:26px}

  /* front of card */
  .card--front{top:515px;background:var(--card-face)}
  .stripes{position:absolute;inset:0;display:flex;flex-direction:column}
  .stripes span{flex:1}
  .stripes span:nth-child(odd){background:var(--stripe-light)}
  .stripes span:nth-child(even){background:var(--stripe-dark)}
  .canton{position:absolute;left:0;top:0;width:360px;height:248px;background:var(--canton)}

  .wordmark{position:absolute;left:36px;top:38px;font-weight:700;font-size:40px;letter-spacing:2px;color:var(--white)}
  .person{position:absolute;left:36px;top:122px}
  .person__name{font-weight:700;font-size:28px;letter-spacing:1.5px;color:var(--green)}
  .person__title{font-size:18px;color:var(--text);margin-top:2px}

  .address{position:absolute;left:36px;top:214px;font-size:18px;line-height:25px;color:var(--text);letter-spacing:.5px}

  .contacts{position:absolute;left:36px;top:290px;list-style:none}
  .contacts li{display:flex;align-items:center;gap:14px;font-size:18px;color:var(--text);height:28px;letter-spacing:.5px}
  .contacts svg{width:16px;height:16px;fill:var(--green);flex:none}
  .contacts .accent{color:var(--green)}

  .mark{position:absolute;right:60px;top:30px;width:400px;height:400px;border-radius:40px;background:var(--mark-fill);border:16px solid var(--frame-gray)}
</style>
</head>
<body>

  <section class="card card--back" aria-label="Card back">
    <div class="faint-square" aria-hidden="true"></div>
    <div class="brand">
      <div class="brand__square" aria-hidden="true"></div>
      <span class="brand__name">RIDGELINE INC</span>
    </div>
  </section>

  <section class="card card--front" aria-label="Card front">
    <div class="stripes" aria-hidden="true">
      <span></span><span></span><span></span><span></span><span></span><span></span><span></span>
      <span></span><span></span><span></span><span></span><span></span><span></span>
    </div>
    <div class="canton" role="img" aria-label="Flag star field in dark tones"></div>

    <div class="wordmark">RIDGELINE INC</div>

    <div class="person">
      <div class="person__name">DANIEL BROOKS</div>
      <div class="person__title">Ceo &amp; Founder</div>
    </div>

    <div class="address">Your Street Address,<br>Country, 1234</div>

    <ul class="contacts">
      <li>
        <svg viewBox="0 0 16 16"><path d="M3 1l3 3-1.5 2c1 2 2.5 3.5 4.5 4.5L11 9l3 3-2 2C6 13 2 9 1 3z"/></svg>
        +000 45 10 258
      </li>
      <li>
        <svg viewBox="0 0 16 16"><path d="M4 0h8v16H4zM5.5 2v10h5V2zM7 13.5h2v1H7z" fill-rule="evenodd"/></svg>
        +000 85 25 111
      </li>
      <li>
        <svg viewBox="0 0 16 16"><path d="M4 1h7v4H4zM1 6h14v7h-3v2H4v-2H1zM5 11v3h6v-3z" fill-rule="evenodd"/></svg>
        +000 85 25 122
      </li>
      <li>
        <svg viewBox="0 0 16 16"><path d="M1 3h14v10H1zM2.5 4.5L8 9l5.5-4.5v-.2h-11z" fill-rule="evenodd"/></svg>
        urname@email.com
      </li>
      <li>
        <svg viewBox="0 0 16 16"><circle cx="8" cy="8" r="7"/><path d="M1 8h14M8 1c-3 3-3 11 0 14M8 1c3 3 3 11 0 14" stroke="#1f1f1f" stroke-width="1" fill="none"/></svg>
        <span>www.<span class="accent">websitename</span>.com</span>
      </li>
    </ul>

    <div class="mark" aria-hidden="true"></div>
  </section>

</body>
</html>
```